Awesome Valdren Business Card Project

We would like a double-sided business card. We have a primary PMS color of PMS 1505 and a secondary color of PMS 1495. I would like to include our logo, the secondary S logo, and the QTALX logo on the business card. We will want a spot for the following information.
Marisa Colton
Valdren
Address: 4318 N Fable Avenue Oak Terrace, IL 60291
Email: mcolton@valdren.example
Phone: 312-555-0148
Mobile: (414) 555-0193
Website: www.valdren.example
Contact Information for Business Card
Marisa Colton Valdren Address: 4318 N Fable Avenue Oak Terrace, IL 60291 Email: mcolton@valdren.example Phone: 312-555-0148 Mobile: (414) 555-0193 Website: www.valdren.example

```html
<!DOCTYPE html>
<html lang="en">
<head>
<meta charset="utf-8">
<title>Valdren Business Card</title>
<link rel="stylesheet" href="https://fonts.googleapis.com/css2?family=Open+Sans:wght@300;400;700&display=swap">
<style>
  :root {
    --page: #d9d9d9;
    --card: #1e1e1e;
    --orange: #f47421;
    --orange-light: #f89a3c;
    --ink: #ffffff;
    --pattern-light: #3a3a3a;
    --pattern-mid: #262626;
    --pattern-dark: #161616;
  }
  * { margin: 0; padding: 0; box-sizing: border-box; }
  html, body { width: 1200px; height: 896px; overflow: hidden; }
  body {
    background: var(--page);
    font-family: "Open Sans", sans-serif;
    position: relative;
  }
  .card {
    position: absolute;
    left: 250px;
    width: 700px;
    height: 398px;
    border-radius: 34px;
    background: var(--card);
    overflow: hidden;
  }
  .card--front { top: 30px; }
  .card--back { top: 468px; }

  .wordmark {
    position: absolute;
    left: 30px;
    top: 2px;
    font-size: 80px;
    line-height: 109px;
    font-weight: 300;
    color: var(--orange);
  }
  .brand-symbol {
    position: absolute;
    left: 390px;
    top: 120px;
    width: 240px;
    height: 240px;
    border-radius: 50%;
    background: var(--orange);
  }
  .accent-bar {
    position: absolute;
    left: 0;
    top: 130px;
    width: 22px;
    height: 50px;
    background: var(--orange);
  }
  .person-name {
    position: absolute;
    left: 33px;
    top: 124px;
    font-size: 30px;
    font-weight: 700;
    color: var(--orange);
  }
  .company {
    position: absolute;
    left: 33px;
    top: 161px;
    font-size: 18px;
    color: var(--ink);
  }
  .contact-list {
    position: absolute;
    left: 28px;
    top: 196px;
    list-style: none;
  }
  .contact-list li {
    display: flex;
    align-items: center;
    height: 26.5px;
    font-size: 18.5px;
    color: var(--ink);
  }
  .contact-list svg {
    width: 14px;
    height: 14px;
    margin-right: 11px;
    fill: var(--orange);
    flex: none;
  }
  .address {
    position: absolute;
    left: 28px;
    top: 315px;
    font-size: 18.5px;
    line-height: 27px;
    color: var(--ink);
    font-style: normal;
  }

  .back-pattern {
    position: absolute;
    inset: 0;
    background:
      radial-gradient(ellipse at 10% 30%, var(--pattern-light) 0%, transparent 55%),
      linear-gradient(120deg, var(--pattern-light) 0%, var(--pattern-mid) 40%, var(--pattern-dark) 75%, var(--pattern-dark) 100%);
  }
  .back-wordmark {
    position: absolute;
    left: 478px;
    top: 318px;
    font-size: 36px;
    line-height: 48px;
    font-weight: 300;
    color: var(--orange);
  }
</style>
</head>
<body>
  <section class="card card--front" aria-label="Card front">
    <div class="wordmark">Valdren</div>
    <div class="brand-symbol" role="img" aria-label="Large brand symbol area"></div>
    <div class="accent-bar"></div>
    <h1 class="person-name">Marisa Colton</h1>
    <p class="company">Valdren</p>
    <ul class="contact-list">
      <li>
        <svg viewBox="0 0 14 14" aria-hidden="true"><path d="M4 0h6a1 1 0 0 1 1 1v12a1 1 0 0 1-1 1H4a1 1 0 0 1-1-1V1a1 1 0 0 1 1-1zm.6 1.6v9.4h4.8V1.6z"/></svg>
        (414) 555-0193
      </li>
      <li>
        <svg viewBox="0 0 14 14" aria-hidden="true"><path d="M3 1l2.2 2.6-1.2 1.6c.8 1.8 2.2 3.2 4 4l1.6-1.2L12.2 10.2 11 12.6C6 12.2 1.8 8 1.4 3z"/></svg>
        312-555-0148
      </li>
      <li>
        <svg viewBox="0 0 14 14" aria-hidden="true"><path d="M1 3h12v1.2L7 8 1 4.2zm0 2.6l6 3.8 6-3.8V11H1z"/></svg>
        mcolton@valdren.example
      </li>
      <li>
        <svg viewBox="0 0 14 14" aria-hidden="true"><circle cx="7" cy="7" r="6"/><path d="M4 4.5c1.5.5 2 1.5 1.5 3 1 .5 1.5 1.5 1 3M9 3c-.5 1 0 2 1.5 2.2" stroke="#1e1e1e" stroke-width="1.2" fill="none"/></svg>
        www.valdren.example
      </li>
    </ul>
    <address class="address">4318 N Fable Avenue<br>Oak Terrace, IL 60291</address>
  </section>

  <section class="card card--back" aria-label="Card back">
    <div class="back-pattern" role="img" aria-label="Repeating brand name pattern in grey, fading to black across the card"></div>
    <div class="back-wordmark">Valdren</div>
  </section>
</body>
</html>
```